Business Cards/Stationary/Letterhead for Crestline Weight Loss Center
Be Healthy, Be Fit, and Be Ready to Lose Weight!
Creative Brief
Simple
Derek Tolsan, PA
Physician Assistant, Co-founder
52816 Birchwood Lane Fremont, CA 94592-7731
CrestlineSlim@mailhaven.example
www.crestlineslim.example
Aim for Results with Crestline Weight Loss! HCG, Appetite Suppressants,B12/B-Complex injections, Menu Plans, Exercise Plans, Nutriceuticals, Supplements.
Present this card to a friend; If your friend signs up, you will receive a 20% discount. The referrals are endless. If you refer 5 friends who sign up then you will receive 100% discount on your next visit. Just make sure your friend puts your name down in the "referral" section of the information sheet and you will be that much closer to saving. (Discount will only apply to weight loss program, discount only applicable for one month or week supply of medication. Non-transferrable. Referral cannot be an existing patient.) Appointment Date: _________ Time: _____

```html
<!DOCTYPE html>
<html lang="en">
<head>
<meta charset="utf-8">
<title>Crestline Weight Loss Center – Stationery Set</title>
<link rel="stylesheet" href="https://fonts.googleapis.com/css2?family=Open+Sans:wght@400;600;700&display=swap">
<style>
:root{
  --backdrop:#d6d6d6;
  --paper:#ffffff;
  --ink:#1b1b1b;
  --orange:#ec7a1c;
  --green:#8dc63f;
  --green-dark:#5f9b2a;
  --grey-text:#6d6d6d;
  --faint:#eef3e6;
}
*{box-sizing:border-box;margin:0;padding:0}
html,body{width:1200px;height:459px;overflow:hidden}
body{background:var(--backdrop);font-family:"Open Sans",Arial,sans-serif;position:relative}
.piece{position:absolute;background:var(--paper);overflow:hidden;box-shadow:0 1px 3px rgba(0,0,0,.25)}
.piece svg.wave{position:absolute;left:0;width:100%;display:block}
.brand{position:absolute;display:flex;align-items:center;gap:3px;font-weight:700;color:var(--orange);white-space:nowrap}
.brand .dot{width:7px;height:7px;border-radius:50%;background:var(--green);flex:none}
.brand.small{font-size:4.5px}
.brand.mid{font-size:6px}
.brand.stack{flex-direction:column;gap:2px;text-align:center}
.brand.stack .dot{width:12px;height:12px}
.small-text{position:absolute;font-size:3px;line-height:1.45;color:var(--grey-text);white-space:nowrap}
.faint-mark{position:absolute;border-radius:50%;background:var(--faint)}
.envelope-back{left:12px;top:12px;width:276px;height:80px;background:var(--ink)}
.envelope-front{left:12px;top:96px;width:276px;height:94px}
.slip-top{left:24px;top:198px;width:264px;height:118px}
.slip-bottom{left:24px;top:330px;width:264px;height:120px}
.card{top:28px;width:96px;height:68px}
.card.dark{background:var(--ink)}
.letterhead{width:222px;height:340px}
.lh-one{left:307px;top:107px}
.lh-two{left:548px;top:107px}
.lh-four{left:950px;top:112px;width:226px;height:308px}
.lh-three{left:792px;top:127px;width:216px;height:323px}
.body-lines{position:absolute;left:22px;right:22px;top:120px;font-size:3px;color:#b9b9b9;line-height:1.6}
</style>
</head>
<body>

<!-- envelope, back flap -->
<div class="piece envelope-back">
  <svg class="wave" style="top:0;height:80px" viewBox="0 0 276 80" preserveAspectRatio="none">
    <path d="M0 58 Q138 78 276 58 L276 80 L0 80Z" fill="#2a2a2a"/>
  </svg>
  <div class="brand stack small" style="left:118px;top:16px"><span class="dot"></span>Crestline Weight Loss Center</div>
</div>

<!-- envelope, front -->
<div class="piece envelope-front">
  <svg class="wave" style="top:0;height:94px" viewBox="0 0 276 94" preserveAspectRatio="none">
    <path d="M0 0 L138 40 L276 0" fill="none" stroke="#e2e2e2" stroke-width="1"/>
  </svg>
</div>

<!-- compliment slip, top -->
<div class="piece slip-top">
  <div class="brand stack small" style="left:12px;top:12px"><span class="dot"></span>Crestline Weight Loss Center</div>
  <div class="small-text" style="left:14px;top:46px">52816 Birchwood Lane Fremont, CA 94592-7731<br>www.crestlineslim.example</div>
  <svg class="wave" style="bottom:0;height:40px" viewBox="0 0 264 40" preserveAspectRatio="none">
    <path d="M0 30 C80 8 170 42 264 14 L264 40 L0 40Z" fill="var(--orange)"/>
    <path d="M0 26 C80 4 170 38 264 10" fill="none" stroke="var(--green)" stroke-width="3"/>
  </svg>
</div>

<!-- compliment slip, bottom -->
<div class="piece slip-bottom">
  <div class="brand stack small" style="left:12px;top:12px"><span class="dot"></span>Crestline Weight Loss Center</div>
  <div class="small-text" style="left:14px;top:46px">CrestlineSlim@mailhaven.example</div>
  <svg class="wave" style="bottom:0;height:52px" viewBox="0 0 264 52" preserveAspectRatio="none">
    <path d="M0 22 C90 2 170 46 264 18 L264 52 L0 52Z" fill="var(--orange)"/>
    <path d="M0 16 C90 -4 170 40 264 12 L264 20 C170 48 90 6 0 26Z" fill="var(--green)"/>
  </svg>
</div>

<!-- business cards -->
<div class="piece card" style="left:293px">
  <div class="brand small" style="left:6px;top:6px"><span class="dot"></span>Crestline Weight Loss</div>
  <div class="small-text" style="left:30px;top:22px">Derek Tolsan, PA<br>Physician Assistant, Co-founder<br>52816 Birchwood Lane<br>Fremont, CA 94592-7731<br>www.crestlineslim.example</div>
  <svg class="wave" style="bottom:0;height:10px" viewBox="0 0 96 10" preserveAspectRatio="none"><path d="M0 6 Q48 0 96 6 L96 10 L0 10Z" fill="var(--orange)"/></svg>
</div>
<div class="piece card dark" style="left:396px">
  <div class="piece" style="left:6px;top:8px;width:84px;height:52px;box-shadow:none;border-radius:3px">
    <div class="brand small" style="left:5px;top:5px"><span class="dot"></span>Crestline Weight Loss</div>
    <div class="small-text" style="left:26px;top:18px">Derek Tolsan, PA<br>Physician Assistant<br>CrestlineSlim@mailhaven.example</div>
  </div>
</div>
<div class="piece card" style="left:520px">
  <div class="brand small" style="left:6px;top:6px"><span class="dot"></span>Crestline Weight Loss</div>
  <div class="small-text" style="left:30px;top:22px">Derek Tolsan, PA<br>Physician Assistant, Co-founder<br>Fremont, CA 94592-7731</div>
  <svg class="wave" style="bottom:0;height:14px" viewBox="0 0 96 14" preserveAspectRatio="none"><path d="M0 4 Q48 14 96 4 L96 14 L0 14Z" fill="var(--ink)"/><path d="M0 2 Q48 12 96 2" stroke="var(--green)" stroke-width="1.5" fill="none"/></svg>
</div>
<div class="piece card" style="left:626px">
  <div class="brand small" style="left:6px;top:6px"><span class="dot"></span>Crestline Weight Loss</div>
  <div class="small-text" style="left:30px;top:22px">Derek Tolsan, PA<br>Physician Assistant, Co-founder<br>www.crestlineslim.example</div>
  <svg class="wave" style="bottom:0;height:14px" viewBox="0 0 96 14" preserveAspectRatio="none"><path d="M0 6 Q48 14 96 4 L96 14 L0 14Z" fill="var(--ink)"/></svg>
</div>
<div class="piece card" style="left:742px">
  <svg class="wave" style="top:0;height:16px" viewBox="0 0 96 16" preserveAspectRatio="none"><path d="M0 0 L96 0 L96 8 Q48 18 0 8Z" fill="var(--orange)"/></svg>
  <div class="small-text" style="left:8px;top:22px;font-size:3.6px;color:var(--green-dark);font-weight:600;white-space:normal;width:80px">Aim for Results with Crestline Weight Loss!</div>
  <div class="small-text" style="left:8px;top:34px;white-space:normal;width:80px">HCG, Appetite Suppressants, B12/B-Complex injections, Menu Plans, Exercise Plans</div>
</div>
<div class="piece card" style="left:850px;width:100px;border-radius:4px">
  <svg class="wave" style="top:0;height:16px" viewBox="0 0 100 16" preserveAspectRatio="none"><path d="M0 0 L100 0 L100 6 Q50 16 0 6Z" fill="var(--green)"/></svg>
  <div class="small-text" style="left:6px;top:18px;white-space:normal;width:88px;font-size:2.6px">Present this card to a friend; If your friend signs up, you will receive a 20% discount. The referrals are endless.<br>Appointment Date: _________ Time: _____</div>
</div>

<!-- letterhead with top wave -->
<div class="piece letterhead lh-one">
  <svg class="wave" style="top:0;height:40px" viewBox="0 0 222 40" preserveAspectRatio="none">
    <path d="M0 0 L222 0 L222 8 C150 30 70 2 0 28Z" fill="var(--ink)"/>
    <path d="M0 28 C70 2 150 30 222 8" fill="none" stroke="var(--green)" stroke-width="3"/>
    <path d="M0 33 C70 7 150 35 222 13" fill="none" stroke="var(--orange)" stroke-width="3"/>
  </svg>
  <div class="brand stack mid" style="left:14px;top:40px"><span class="dot"></span>Crestline Weight Loss Center</div>
  <div class="small-text" style="left:120px;top:46px">52816 Birchwood Lane Fremont, CA 94592-7731<br>CrestlineSlim@mailhaven.example</div>
  <div class="faint-mark" style="left:56px;top:120px;width:110px;height:110px"></div>
</div>

<!-- letterhead with bottom wave -->
<div class="piece letterhead lh-two">
  <div class="brand stack mid" style="left:14px;top:14px"><span class="dot"></span>Crestline Weight Loss Center</div>
  <div class="small-text" style="left:120px;top:20px">52816 Birchwood Lane Fremont, CA 94592-7731<br>www.crestlineslim.example</div>
  <div class="faint-mark" style="left:56px;top:110px;width:110px;height:110px"></div>
  <svg class="wave" style="bottom:0;height:44px" viewBox="0 0 222 44" preserveAspectRatio="none">
    <path d="M0 12 C80 40 150 4 222 22 L222 44 L0 44Z" fill="var(--ink)"/>
    <path d="M0 8 C80 36 150 0 222 18" fill="none" stroke="var(--orange)" stroke-width="3"/>
  </svg>
</div>

<!-- letterhead behind, right -->
<div class="piece lh-four">
  <div class="brand stack mid" style="left:150px;top:14px"><span class="dot"></span>Crestline Weight Loss</div>
  <div class="faint-mark" style="left:120px;top:100px;width:100px;height:100px"></div>
</div>

<!-- letterhead, dark bottom band -->
<div class="piece lh-three">
  <div class="brand stack mid" style="left:76px;top:16px"><span class="dot"></span>Crestline Weight Loss Center</div>
  <div class="faint-mark" style="left:53px;top:105px;width:110px;height:110px"></div>
  <svg class="wave" style="bottom:0;height:48px" viewBox="0 0 216 48" preserveAspectRatio="none">
    <path d="M0 20 C70 0 150 36 216 10 L216 48 L0 48Z" fill="var(--ink)"/>
    <path d="M0 16 C70 -4 150 32 216 6" fill="none" stroke="var(--green)" stroke-width="2.5"/>
  </svg>
  <div class="small-text" style="left:40px;bottom:10px;color:#cfcfcf">52816 Birchwood Lane Fremont, CA 94592-7731 · www.crestlineslim.example</div>
</div>

</body>
</html>
```